Social Media designs (LinkedIn banner, LinkedIn posts, Instagram)

Hello designers!
We are looking to create some more concepts for our social media identity for a search firm (recruitment company)
I have attached a "brand toolkit" that shows our brand, logo, colour scheme to guide you with regards to colours and identiy.

You will see in the brand toolkit there are some examples of;
- A LinkedIn banner for the company (page 23)
- Social Media posts for LinkedIn and Instagram (page 21)

What we are looking for...

We don't really like the current LinkedIn banner ideas. We would like to see more concepts that look more aesthetically pleasing - the current ideas look quite dull.

We DO like the social media post concepts but we would like to have more templates/options that we can use (similar themes)

We welcome submissions for Social Media designs that we can use with our company branding. Thank you for your work in advance!

```html
<!DOCTYPE html>
<html lang="en">
<head>
<meta charset="utf-8">
<title>Harlow Reid – Social Media Templates</title>
<link href="https://fonts.googleapis.com/css2?family=Outfit:wght@300;400;500;600&display=swap" rel="stylesheet">
<style>
:root{
  --forest:#182824;
  --sage:#468a70;
  --sage-bright:#4f9a7c;
  --cream:#e2e2d8;
  --white:#ffffff;
}
*{margin:0;padding:0;box-sizing:border-box}
html,body{width:1134px;height:1200px;overflow:hidden;background:var(--white)}
body{position:relative;font-family:"Outfit",sans-serif;color:var(--cream)}
.post{position:absolute;width:505px;height:505px;overflow:hidden}
.post--profile{left:45px;top:71px;background:var(--sage)}
.post--vacancy{left:583px;top:71px;background:var(--forest)}
.post--office{left:45px;top:612px;background:var(--forest)}
.post--about{left:583px;top:612px;background:var(--forest)}
.abs{position:absolute}
.deco{position:absolute;left:0;top:0;width:505px;height:505px;pointer-events:none}
.brand{display:flex;align-items:center;gap:8px;font-weight:500;line-height:.95}
.brand__mark{flex:none}
.photo{position:absolute}

/* profile */
.profile__top{left:135px;top:0;width:370px;height:99px;background:var(--cream)}
.profile__brand{left:8px;top:17px;width:114px;height:50px;background:var(--cream);padding:0 10px;color:var(--forest);font-size:16px}
.profile__brand .brand__mark{width:14px;height:14px;background:var(--sage)}
.profile__panel{left:7px;top:99px;width:310px;height:277px;background:var(--forest)}
.profile__name{left:16px;top:134px;font-size:50px;font-weight:500;letter-spacing:-.5px;line-height:1}
.profile__role{left:18px;top:196px;font-size:21px;font-weight:400}
.profile__contact{left:19px;top:247px;font-size:20px;font-weight:300;line-height:25px}
.profile__tag{left:20px;top:344px;font-size:13.5px;font-weight:400}
.office{font-size:12.5px;font-weight:300;line-height:16px}
.profile__office-us{left:21px;top:388px}
.profile__office-emea{left:21px;top:443px}

/* vacancy */
.vacancy__brand{left:30px;top:18px;font-size:17px;color:var(--cream)}
.vacancy__brand .brand__mark{width:20px;height:20px;background:var(--cream)}
.vacancy__tagline{right:28px;top:16px;text-align:right;font-size:17.5px;font-weight:500;line-height:19px}
.vacancy__title{left:30px;top:66px;font-size:40px;font-weight:500;line-height:43px;letter-spacing:-.2px}
.vacancy__location{left:31px;top:147px;font-size:20.5px;font-weight:500;color:var(--sage-bright)}

/* office */
.office__brandbox{left:271px;top:0;width:234px;height:101px;background:var(--cream);display:flex;align-items:center;justify-content:flex-end;padding-right:15px}
.office__brand{color:var(--forest);font-size:31px;font-weight:500}
.office__brand .brand__mark{width:42px;height:42px;background:var(--sage);margin-right:10px}
.office__body{left:271px;top:101px;width:234px;height:404px;background:var(--sage);text-align:right;padding-right:18px}
.office__services{position:absolute;right:17px;top:19px;font-size:19px;font-weight:500;line-height:24px}
.office__intro{position:absolute;right:18px;top:120px;width:200px;font-size:12.5px;font-weight:300;line-height:15px}
.office__location{position:absolute;right:18px;top:213px;font-size:19px;font-weight:500;line-height:24px;color:var(--forest)}
.office__rule{position:absolute;left:10px;top:293px;width:224px;height:1.5px;background:var(--forest)}
.office__contacts{position:absolute;right:19px;top:301px;font-size:11.5px;line-height:12.5px;font-weight:300}
.office__contacts em{font-style:italic;color:var(--forest);font-weight:400}
.office__contacts .gap{height:12px}

/* about */
.about__card{left:15px;top:209px;width:283px;height:282px;background:var(--cream);color:var(--forest);padding:14px 16px}
.about__name{font-size:33px;font-weight:500;line-height:1;letter-spacing:-.2px}
.about__text{margin-top:10px;font-size:15px;font-weight:300;line-height:20.6px}
.about__cta{margin-top:14px;font-size:22px;font-weight:500;color:var(--sage)}
.about__contact{margin-top:4px;font-size:20.5px;font-weight:400;line-height:23px}
.about__brand{left:333px;top:417px;font-size:24px;color:var(--cream)}
.about__brand .brand__mark{width:30px;height:30px;background:var(--sage);margin-right:6px}
</style>
</head>
<body>

<!-- Profile card -->
<section class="post post--profile">
  <div class="abs profile__top"></div>
  <svg class="deco" viewBox="0 0 505 505"><circle cx="505" cy="500" r="452" fill="var(--sage)"/><circle cx="505" cy="470" r="250" fill="var(--cream)"/></svg>
  <div class="abs brand profile__brand"><span class="brand__mark"></span><span>Harlow<br>Reid</span></div>
  <div class="abs profile__panel"></div>
  <svg class="deco" viewBox="0 0 505 505" fill="none" stroke="var(--sage)" stroke-width="1"><line x1="135" y1="99" x2="135" y2="376"/><path d="M320 100 C250 160 230 260 235 330 L320 330"/></svg>
  <svg class="photo" style="left:0;top:0" width="505" height="505" viewBox="0 0 505 505" role="img" aria-label="Portrait photo of the group managing director in a white shirt">
    <defs><linearGradient id="portrait" x1="0" y1="0" x2="0" y2="1"><stop offset="0" stop-color="#cfc6bd"/><stop offset=".45" stop-color="#e8e4df"/><stop offset="1" stop-color="#f2f2f0"/></linearGradient></defs>
    <path d="M325 95 Q380 55 435 85 Q470 120 460 200 Q505 250 505 300 L505 505 L205 505 Q230 420 300 380 Q330 320 320 230 Q305 140 325 95Z" fill="url(#portrait)"/>
  </svg>
  <div class="abs profile__name">Owen Marsh</div>
  <div class="abs profile__role">Group Managing Director</div>
  <div class="abs profile__contact">+44 0100 000 111<br>omarsh@harlowreid.com</div>
  <div class="abs profile__tag">Talent knows no border</div>
  <div class="abs office profile__office-us">US Office<br>+1 212 555 0148<br>hello@harlowreid.com</div>
  <div class="abs office profile__office-emea">EMEA/APAC<br>+44 (0)20 7946 0321<br>hello@harlowreid.com</div>
</section>

<!-- Vacancy post -->
<section class="post post--vacancy">
  <svg class="deco" viewBox="0 0 505 505" fill="none" stroke="var(--sage)" stroke-width="1.2"><line x1="131" y1="0" x2="131" y2="60"/><path d="M395 0 Q250 200 270 505"/><path d="M505 145 Q470 190 460 260"/><path d="M505 480 Q470 440 455 400"/><line x1="478" y1="315" x2="505" y2="315"/></svg>
  <div class="abs brand vacancy__brand"><span class="brand__mark"></span><span>Harlow<br>Reid</span></div>
  <div class="abs vacancy__tagline">Talent Knows<br>No Border</div>
  <div class="abs vacancy__title">Case Manager<br>Enhanced Due Diligence</div>
  <div class="abs vacancy__location">London, United Kingdom</div>
  <div class="photo" role="img" aria-label="Looking up at glass skyscrapers in the City of London" style="left:29px;top:190px;width:293px;height:293px;background:linear-gradient(160deg,#5d6a73,#c9ccd0 45%,#6e6f72 80%,#3a3b3e)"></div>
  <div class="photo" role="img" aria-label="Ornate historic stone building against a blue sky" style="left:337px;top:190px;width:141px;height:141px;background:linear-gradient(180deg,#a9c6de,#cdbba4 55%,#5e5548)"></div>
  <div class="photo" role="img" aria-label="Angular modern roof with glass panels at dusk" style="left:337px;top:343px;width:141px;height:141px;background:linear-gradient(180deg,#93a4ba,#c7a58a 40%,#4b4846)"></div>
</section>

<!-- Office post -->
<section class="post post--office">
  <svg class="deco" viewBox="0 0 505 505" fill="none" stroke="var(--sage)" stroke-width="1.2"><line x1="10" y1="0" x2="10" y2="505"/><line x1="172" y1="0" x2="172" y2="21"/><line x1="246" y1="305" x2="271" y2="305"/></svg>
  <div class="photo" role="img" aria-label="Modern office corridor with glass partitions and meeting room" style="left:23px;top:21px;width:223px;height:464px;background:linear-gradient(180deg,#f1f1f0,#d6d6d4 40%,#8b8b89 75%,#b5b5b3)"></div>
  <div class="abs office__brandbox"><div class="brand office__brand"><span class="brand__mark"></span><span>Harlow<br>Reid</span></div></div>
  <div class="abs office__body">
    <div class="office__services">Executive Search,<br>Recruitment &amp; Interim<br>Talent Solutions</div>
    <div class="office__intro">We're an Executive Search &amp; Recruitment firm that helps ambitious organisations to hire exceptional people worldwide.</div>
    <div class="office__location">Staffing and<br>Recruiting London</div>
    <div class="office__rule"></div>
    <div class="office__contacts"><em>US Office</em><br>+1 212 555 0148<br>hello@harlowreid.com<div class="gap"></div><em>EMEA/APAC</em><br>+44 (0)20 7946 0321<br>hello@harlowreid.com</div>
  </div>
</section>

<!-- About post -->
<section class="post post--about">
  <svg class="deco" viewBox="0 0 505 505" fill="none" stroke="var(--sage)" stroke-width="1.2"><line x1="62" y1="0" x2="62" y2="209"/><path d="M325 0 Q300 10 295 20"/><path d="M372 360 Q390 450 485 505"/><line x1="487" y1="318" x2="505" y2="318"/><path d="M230 491 Q240 500 245 505"/></svg>
  <div class="photo" role="img" aria-label="Domed cathedral framed by reflective glass towers" style="left:147px;top:19px;width:340px;height:340px;background:linear-gradient(180deg,#8fb3b4,#a69785 45%,#6e5a48 80%,#8e8c85)"></div>
  <div class="abs about__card">
    <div class="about__name">Harlow Reid</div>
    <div class="about__text">is a global executive search and recruitment firm, supporting ambitious organisations to recruit exceptional individuals in all corners of the world</div>
    <div class="about__cta">Contact us today at</div>
    <div class="about__contact">info@harlowreid.com<br>or via phone;</div>
  </div>
  <div class="abs brand about__brand"><span class="brand__mark"></span><span>Harlow<br>Reid</span></div>
</section>

</body>
</html>
```